Custom Made Digital Jukebox sales and rental website

I need a design for a Custom Made Digital Jukebox sales and rental services website. Domain name is quelitrune.com. Exisiting customer shall have a section to register, login/logout, my account, support. All other visitor shall have at least the following options or menu avaialble: Home, FAQ, Services, Products, and Contact us. I have attached a high level requirements pdf file. Please don't be limited by high level requirements file attached, your idea may be better than what I specified. My products are designed base on customer requirements. Common parts are: Bill and Coin Acceptors, Touchscreen or keypad. All of them are wall mount.

Target Market(s)

Custom made digital Jukebox for Home and Commercial use

Industry/Entity Type

Digital

Number of Pages Required

1 page

Requirements
Must have
• PSD required.
Nice to have
• HTML code and CSS Stylesheet
• Logo for QueliTrune
• Inner Pages
Should not have
• Copyright material from related websites, previously developed or any other.

```html
<!DOCTYPE html>
<html lang="en">
<head>
<meta charset="utf-8">
<title>QueliTrune – Custom Digital Jukeboxes</title>
<link href="https://fonts.googleapis.com/css2?family=Oswald:wght@400;500;600&family=Open+Sans:wght@400;600;700&display=swap" rel="stylesheet">
<style>
:root{
  --red:#e8473a;
  --ink:#1f1f1f;
  --charcoal:#2a2a2a;
  --panel:#242424;
  --grey-bg:#ededed;
  --light:#f6f6f6;
  --text:#444;
  --muted:#888;
  --white:#fff;
}
*{box-sizing:border-box;margin:0;padding:0}
html,body{width:1200px;height:2552px;overflow:hidden}
body{font-family:"Open Sans",Arial,sans-serif;color:var(--text);background:var(--white)}
.site{width:1200px;height:2552px;position:relative}

/* header */
.header{height:140px;background:linear-gradient(#1a1a1a,#2b2b2b);position:relative;color:var(--white)}
.brand{position:absolute;left:54px;top:38px;display:flex;align-items:center;gap:12px}
.brand-dot{width:22px;height:22px;border-radius:50%;background:var(--red)}
.brand-name{font-family:"Oswald",sans-serif;font-weight:600;font-size:44px;line-height:1;letter-spacing:1px;color:var(--white)}
.account{position:absolute;right:60px;top:2px;display:flex;gap:10px}
.account a{font-size:13px;color:var(--white);text-decoration:none;border:1px solid #666;padding:3px 12px;background:#333}
.utility{position:absolute;right:60px;top:52px;display:flex;align-items:center;gap:28px;font-size:15px}
.utility .contact{display:flex;gap:8px;align-items:center;color:#ddd}
.utility .phone{font-size:22px;font-weight:600;color:var(--white)}
.nav{position:absolute;left:440px;bottom:0;display:flex}
.nav a{font-family:"Oswald",sans-serif;font-size:19px;letter-spacing:1px;color:var(--white);text-decoration:none;padding:0 26px 20px;position:relative}
.nav a.active::after{content:"";position:absolute;left:0;right:0;bottom:0;height:5px;background:var(--red)}

/* hero */
.hero{height:520px;position:relative;background:radial-gradient(ellipse at 55% 40%,#a66c2a 0%,#5a3a1c 35%,#1c1410 75%)}
.hero .art{position:absolute;left:440px;top:20px;width:360px;height:440px;border-radius:170px 170px 20px 20px;background:linear-gradient(#f2d36b,#d6942e 60%,#7a4a1c)}
.hero-caption{position:absolute;left:0;right:0;bottom:0;height:100px;background:linear-gradient(transparent,rgba(0,0,0,.75));display:flex;align-items:center;padding-left:186px;font-family:"Oswald",sans-serif;font-weight:600;font-size:34px;white-space:nowrap;color:var(--white)}

/* how it works */
.how{height:390px;background:var(--grey-bg);position:relative}
.section-title{font-family:"Oswald",sans-serif;font-weight:500;font-size:38px;color:var(--ink);text-align:center;letter-spacing:1px}
.how .section-title{padding-top:24px;position:relative}
.how svg{position:absolute;left:0;top:0}
.step-label{position:absolute;font-family:"Oswald",sans-serif;font-size:18px;color:var(--ink);text-align:center;width:240px;line-height:1.25}

/* offers */
.offers{height:410px;background:var(--white);position:relative}
.offer{position:absolute;top:26px;width:300px;height:360px;text-align:center;color:var(--white)}
.offer svg{position:absolute;left:0;top:0}
.offer .body{position:relative;padding:90px 44px 0}
.offer h2{font-family:"Oswald",sans-serif;font-weight:500;font-size:52px;line-height:1;color:var(--white)}
.offer h3{font-family:"Oswald",sans-serif;font-weight:400;font-size:24px;color:var(--red);line-height:1.1;margin-top:4px}
.offer p{font-size:13px;line-height:1.5;margin-top:14px;color:#ddd}
.offer.rent .body{padding-top:74px}

/* features */
.features{height:270px;background:var(--light);position:relative}
.tabs{position:absolute;left:135px;top:50px;display:flex}
.tab{width:200px;height:42px;display:flex;align-items:center;justify-content:center;font-weight:700;font-size:17px;color:var(--white)}
.tab.key{background:var(--red)}
.tab.benefits{background:var(--charcoal);margin-left:8px}
.feature-box{position:absolute;left:135px;top:92px;width:930px;height:140px;background:var(--white);border:1px solid #ddd;display:grid;grid-template-columns:1fr 1fr;padding:20px 30px;row-gap:6px;column-gap:40px}
.feature-box li{list-style:none;font-size:14px;display:flex;align-items:center;gap:10px;color:var(--text)}

/* products */
.products{height:730px;background:var(--white);position:relative}
.products .section-title{padding-top:34px}
.product-grid{position:absolute;left:138px;top:104px;display:grid;grid-template-columns:repeat(3,300px);column-gap:12px;row-gap:18px}
.product{width:300px;height:290px;position:relative}
.product .art{height:206px;background:radial-gradient(circle at 50% 45%,#555 0%,#1a1a1a 70%);position:relative}
.product .shape{position:absolute;left:112px;top:26px;width:76px;height:160px;border-radius:38px 38px 6px 6px}
.product .caption{height:70px;background:var(--light);text-align:center;padding-top:12px}
.product .caption strong{display:block;font-size:15px;color:var(--ink);font-weight:600}
.product .caption span{font-size:12px;color:var(--muted)}
.product.featured .caption{background:var(--red)}
.product.featured .caption strong,.product.featured .caption span{color:var(--white)}
.product .more{position:absolute;left:138px;bottom:0;width:24px;height:24px;border-radius:50%;background:var(--white);border:1px solid #ccc;display:flex;align-items:center;justify-content:center;font-size:16px;font-weight:700;color:var(--ink)}

/* footer */
.footer{height:92px;background:var(--ink);position:absolute;left:0;right:0;bottom:0;color:#bbb;padding:26px 54px;font-size:14px}
.footer nav a{color:var(--white);text-decoration:none}
.footer small{display:block;margin-top:8px;font-size:12px;color:#999}
.follow{position:absolute;right:54px;top:22px;text-align:right;color:var(--white)}
.follow .icons{display:flex;gap:8px;margin-top:8px;justify-content:flex-end}
.follow .icons span{width:20px;height:20px;border-radius:50%;background:#555}
</style>
</head>
<body>
<div class="site">

<header class="header">
  <div class="brand"><span class="brand-dot"></span><span class="brand-name">QueliTrune</span></div>
  <div class="account"><a href="#">Sign Up</a><a href="#">Login</a></div>
  <div class="utility">
    <span class="contact">
      <svg width="16" height="12" viewBox="0 0 16 12"><rect x="0.5" y="0.5" width="15" height="11" fill="none" stroke="#ddd"/><path d="M1 1l7 6 7-6" fill="none" stroke="#ddd"/></svg>
      info@quelitrune.com</span>
    <span class="contact phone">
      <svg width="18" height="18" viewBox="0 0 24 24"><path d="M6.6 10.8a15 15 0 006.6 6.6l2.2-2.2c.3-.3.7-.4 1-.2 1.1.4 2.3.6 3.6.6.6 0 1 .4 1 1V20c0 .6-.4 1-1 1A17 17 0 013 4c0-.6.4-1 1-1h3.5c.6 0 1 .4 1 1 0 1.3.2 2.5.6 3.6.1.3 0 .7-.2 1z" fill="#fff"/></svg>
      555 204 7316</span>
  </div>
  <nav class="nav">
    <a href="#" class="active">HOME</a><a href="#">SERVICES</a><a href="#">PRODUCTS</a><a href="#">FAQ</a><a href="#">CONTACT US</a>
  </nav>
</header>

<section class="hero" role="img" aria-label="Glowing vintage-style digital jukebox in a warmly lit bar">
  <div class="art"></div>
  <div class="hero-caption">Lorem ipsum dolor sit amet, consectetuer adipiscing elit sed</div>
</section>

<section class="how">
  <svg width="1200" height="390" viewBox="0 0 1200 390">
    <path d="M260 190 C330 120 410 110 480 130 C560 150 620 220 700 200 C780 180 860 130 930 140" fill="none" stroke="#bbb" stroke-width="2" stroke-dasharray="6 6"/>
    <g fill="#fff" stroke="#ddd" stroke-width="2">
      <circle cx="260" cy="190" r="42"/><circle cx="480" cy="130" r="42"/><circle cx="700" cy="200" r="42"/><circle cx="930" cy="140" r="42"/>
    </g>
    <g fill="none" stroke="#e8473a" stroke-width="3">
      <circle cx="250" cy="190" r="9"/><circle cx="272" cy="190" r="9"/>
      <rect x="462" y="118" width="36" height="24" rx="3"/><line x1="462" y1="126" x2="498" y2="126"/>
      <circle cx="700" cy="200" r="14"/><path d="M700 182v-6M700 224v-6M682 200h-6M724 200h-6"/>
      <rect x="910" y="128" width="24" height="20"/><path d="M934 134h10l6 8v6h-16"/><circle cx="918" cy="150" r="4"/><circle cx="942" cy="150" r="4"/>
    </g>
  </svg>
  <div class="section-title">HOW IT WORKS</div>
  <div class="step-label" style="left:140px;top:248px">MAKE<br>YOUR ORDER</div>
  <div class="step-label" style="left:360px;top:188px">CHOOSE PAYMENT<br>METHOD</div>
  <div class="step-label" style="left:580px;top:258px">DESIGNED BASE ON<br>REQUIREMENTS</div>
  <div class="step-label" style="left:810px;top:198px">DELIVERY TO YOUR<br>DOOR STEP</div>
</section>

<section class="offers">
  <div class="offer custom" style="left:210px">
    <svg width="300" height="360" viewBox="0 0 300 360"><polygon points="150,0 300,80 300,270 150,350 0,270 0,80" fill="#242424"/><polygon points="138,338 150,352 162,338" fill="#e8473a"/><polygon points="140,350 150,360 160,350" fill="#e8473a"/></svg>
    <div class="body">
      <h2>CUSTOM</h2>
      <h3>Digital Jukebox</h3>
      <p>Lorem ipsum dolor sit amet, consectetuer adipiscing elit, sed diam nonummy nibh euismod tincidunt ut laoreet dolore magna</p>
    </div>
  </div>
  <div class="offer rent" style="left:690px">
    <svg width="300" height="360" viewBox="0 0 300 360"><polygon points="150,0 300,80 300,270 150,350 0,270 0,80" fill="#242424"/><polygon points="138,338 150,352 162,338" fill="#e8473a"/><polygon points="140,350 150,360 160,350" fill="#e8473a"/></svg>
    <div class="body">
      <h3>Get Digital<br>Jukeboxes on</h3>
      <h2>RENT</h2>
      <p>Lorem ipsum dolor sit amet, consectetuer adipiscing elit, sed diam nonummy nibh euismod tincidunt ut laoreet dolore magna</p>
    </div>
  </div>
</section>

<section class="features">
  <div class="tabs"><div class="tab key">Key Features</div><div class="tab benefits">Our Benefits</div></div>
  <ul class="feature-box">
    <li><svg width="14" height="12" viewBox="0 0 14 12"><path d="M1 6l4 4 8-9" fill="none" stroke="#1f1f1f" stroke-width="2.5"/></svg>Lorem ipsum dolor sit amet, consectetuer</li>
    <li><svg width="14" height="12" viewBox="0 0 14 12"><path d="M1 6l4 4 8-9" fill="none" stroke="#1f1f1f" stroke-width="2.5"/></svg>Lorem ipsum dolor sit amet, consectetuer adipiscing elit</li>
    <li><svg width="14" height="12" viewBox="0 0 14 12"><path d="M1 6l4 4 8-9" fill="none" stroke="#1f1f1f" stroke-width="2.5"/></svg>Lorem ipsum dolor sit amet, consectetuer adipiscing</li>
    <li><svg width="14" height="12" viewBox="0 0 14 12"><path d="M1 6l4 4 8-9" fill="none" stroke="#1f1f1f" stroke-width="2.5"/></svg>Lorem ipsum dolor sit amet, consectetuer adipiscing</li>
    <li><svg width="14" height="12" viewBox="0 0 14 12"><path d="M1 6l4 4 8-9" fill="none" stroke="#1f1f1f" stroke-width="2.5"/></svg>Lorem ipsum dolor sit amet, consectetuer adipiscing</li>
    <li><svg width="14" height="12" viewBox="0 0 14 12"><path d="M1 6l4 4 8-9" fill="none" stroke="#1f1f1f" stroke-width="2.5"/></svg>Lorem ipsum dolor sit amet, consectetuer</li>
    <li><svg width="14" height="12" viewBox="0 0 14 12"><path d="M1 6l4 4 8-9" fill="none" stroke="#1f1f1f" stroke-width="2.5"/></svg>Lorem ipsum dolor sit amet, consectetuer adipiscing</li>
    <li><svg width="14" height="12" viewBox="0 0 14 12"><path d="M1 6l4 4 8-9" fill="none" stroke="#1f1f1f" stroke-width="2.5"/></svg>Lorem ipsum dolor sit amet, consectetuer adipiscing elit</li>
  </ul>
</section>

<section class="products">
  <div class="section-title">POPULAR PRODUCTS</div>
  <div class="product-grid">
    <article class="product"><div class="art" role="img" aria-label="Classic arched digital jukebox with orange lights"><div class="shape" style="background:linear-gradient(#e6a24a,#8a4a1c)"></div></div><div class="caption"><strong>Lorem ipsum dolor</strong><span>Lorem Sagittis Tincidunt Aenean Tristique</span></div><span class="more">+</span></article>
    <article class="product featured"><div class="art" role="img" aria-label="Digital jukebox with red and green trim"><div class="shape" style="background:linear-gradient(#c44a3a,#5a7a3a)"></div></div><div class="caption"><strong>Lorem ipsum dolor</strong><span>Lorem Sagittis Tincidunt Aenean Tristique</span></div><span class="more">+</span></article>
    <article class="product"><div class="art" role="img" aria-label="Wood-finished digital jukebox"><div class="shape" style="background:linear-gradient(#c9a06a,#6a4424)"></div></div><div class="caption"><strong>Lorem ipsum dolor</strong><span>Lorem Sagittis Tincidunt Aenean Tristique</span></div><span class="more">+</span></article>
    <article class="product"><div class="art" role="img" aria-label="Tall wall-mount digital jukebox with amber glow"><div class="shape" style="background:linear-gradient(#e8b45a,#7a3e1a)"></div></div><div class="caption"><strong>Lorem ipsum dolor</strong><span>Lorem Sagittis Tincidunt Aenean Tristique</span></div><span class="more">+</span></article>
    <article class="product"><div class="art" role="img" aria-label="Digital jukebox with touchscreen panel"><div class="shape" style="background:linear-gradient(#6ab0d8,#8a3a2a)"></div></div><div class="caption"><strong>Lorem ipsum dolor</strong><span>Lorem Sagittis Tincidunt Aenean Tristique</span></div><span class="more">+</span></article>
    <article class="product"><div class="art" role="img" aria-label="Neon-lit digital jukebox in teal and pink"><div class="shape" style="background:linear-gradient(#5ad0d0,#c04a7a)"></div></div><div class="caption"><strong>Lorem ipsum dolor</strong><span>Lorem Sagittis Tincidunt Aenean Tristique</span></div><span class="more">+</span></article>
  </div>
</section>

<footer class="footer">
  <nav><a href="#">Home</a> / <a href="#">Services</a> / <a href="#">Products</a> / <a href="#">FAQ</a> / <a href="#">Contact Us</a></nav>
  <small>Copyright © 2015 quelitrune.com. All Rights Reserved</small>
  <div class="follow">Follow Us<div class="icons"><span></span><span></span><span></span><span></span></div></div>
</footer>

</div>
</body>
</html>
```